Zielgruppe
Zielgruppe sind Großhändler in der Elektrotechnik, Fachfirmen für Notbeleuchtung. Produkte: Notbeleuchtungssysteme, Not- und Sicherheitsleuchten, Akkumulatoren/Batterien (industrielle)
Aufgabenstellung
Optimale Darstellung des Logos und der Werte des Unternehmens. Einhaltung der Farben des Logos. Eher eine helle Businesskarte, nicht zu Dunkel.
Wir bitten, dass uns der Gewinner gleich für die ersten 6 Mitarbeiter, welche Visitenkarten in unserem Unternehmen benötigen, zu erstellen.
Die bestehende Visitenkarte kam leider nicht gut an. Falsche Farben und kein komplett abgestimmtes Design.
Die neue Visitenkarte soll gut zur Website passen und die Firma optimal repräsentieren.
!Bitte nicht die Farbe der bestehenden Visitenkarte benutzen sondern nur Farbtöne des Logos. Bitte nicht zwingend am bestehenden Design der Visitenkarte orientieren, wir möchten frische Ideen!

```html
<!DOCTYPE html>
<html lang="de">
<head>
<meta charset="utf-8">
<title>Norlux Systems – Visitenkarte</title>
<link rel="stylesheet" href="https://fonts.googleapis.com/css2?family=Source+Sans+3:wght@400;600;700&display=swap">
<style>
  :root {
    --magenta: #d9389b;
    --grey: #8f959c;
    --grey-dark: #767c83;
    --paper: #ffffff;
    --backdrop: #e3e4e5;
  }
  * { margin: 0; padding: 0; box-sizing: border-box; }
  html, body { width: 1200px; height: 901px; overflow: hidden; }
  body {
    background: var(--backdrop);
    font-family: "Source Sans 3", "Segoe UI", sans-serif;
    color: var(--grey);
    position: relative;
  }
  .card {
    position: absolute;
    top: 288px;
    width: 500px;
    height: 324px;
    background: var(--paper);
    box-shadow: 0 6px 18px rgba(0,0,0,0.12);
    overflow: hidden;
  }
  .card--front { left: 70px; }
  .card--back { left: 630px; }

  .wordmark {
    display: flex;
    align-items: center;
    gap: 10px;
    font-weight: 400;
    letter-spacing: 0.14em;
    color: var(--grey);
    font-size: 20px;
    white-space: nowrap;
  }
  .wordmark__square {
    width: 30px; height: 30px;
    border: 3px solid var(--magenta);
    flex: none;
  }
  .card--front .wordmark { position: absolute; left: 34px; top: 36px; }

  .person {
    position: absolute;
    right: 34px;
    top: 100px;
    text-align: right;
    line-height: 1.25;
  }
  .person__name { font-weight: 700; font-size: 20px; color: var(--grey-dark); }
  .person__role { font-size: 10px; color: var(--grey); }
  .person__company { font-size: 12px; margin-top: 6px; }
  .accent-bar {
    position: absolute; right: 0; top: 104px;
    width: 4px; height: 90px; background: var(--magenta);
  }

  .contact {
    position: absolute;
    right: 34px;
    bottom: 28px;
    list-style: none;
    font-size: 12.5px;
    line-height: 1;
  }
  .contact li {
    display: flex; justify-content: flex-end; align-items: center;
    gap: 8px; margin-top: 6px;
  }
  .contact__icon {
    width: 16px; height: 16px; border-radius: 50%;
    background: var(--magenta);
    display: flex; align-items: center; justify-content: center;
  }

  .back__white {
    position: absolute; left: 0; top: 0; width: 270px; height: 100%;
  }
  .back__white .wordmark {
    position: absolute; left: 30px; top: 132px; font-size: 18px;
  }
  .back__url {
    position: absolute; left: 30px; bottom: 26px;
    font-size: 11px; font-weight: 700; color: var(--magenta);
  }
  .back__values {
    position: absolute; right: 0; top: 0; width: 230px; height: 100%;
    background: var(--magenta);
  }
  .value {
    position: absolute; width: 90px; text-align: center;
    color: var(--paper); font-size: 8.5px; font-weight: 700;
    letter-spacing: 0.04em; line-height: 1.2; text-transform: uppercase;
  }
  .value svg { display: block; margin: 0 auto 5px; }
  .value--tech { left: 12px; top: 110px; }
  .value--partner { left: 70px; top: 32px; }
  .value--quality { left: 128px; top: 110px; }
  .value--battery { left: 70px; top: 200px; }
</style>
</head>
<body>

<section class="card card--front" aria-label="Vorderseite">
  <div class="wordmark"><span class="wordmark__square"></span>NORLUX SYSTEMS</div>
  <span class="accent-bar"></span>
  <div class="person">
    <p class="person__name">Lutz Bramer</p>
    <p class="person__role">Geschäftsführer</p>
    <p class="person__role">Managing Director</p>
    <p class="person__company">Norlux Systems GmbH<br>Lindenweg 4<br>D-83000 Seehausen</p>
  </div>
  <ul class="contact">
    <li>08000 12345 67
      <span class="contact__icon"><svg width="9" height="9" viewBox="0 0 10 10"><path d="M2 1l2 2-1 1.2a6 6 0 0 0 2.8 2.8L7 6l2 2-1.2 1.2C4.5 9 1 5.5.8 2.2z" fill="#fff"/></svg></span></li>
    <li>0170-0000000
      <span class="contact__icon"><svg width="9" height="9" viewBox="0 0 10 10"><rect x="2.5" y="0.5" width="5" height="9" rx="1" fill="none" stroke="#fff" stroke-width="1.2"/></svg></span></li>
    <li>lutz.bramer@norlux-systems.com
      <span class="contact__icon"><svg width="9" height="9" viewBox="0 0 10 10"><rect x="0.8" y="2" width="8.4" height="6" fill="none" stroke="#fff" stroke-width="1.1"/><path d="M1 2.5l4 3 4-3" fill="none" stroke="#fff" stroke-width="1.1"/></svg></span></li>
  </ul>
</section>

<section class="card card--back" aria-label="Rückseite">
  <div class="back__white">
    <div class="wordmark"><span class="wordmark__square"></span>NORLUX SYSTEMS</div>
    <p class="back__url">www.norlux-systems.com</p>
  </div>
  <div class="back__values">
    <div class="value value--partner">
      <svg width="34" height="30" viewBox="0 0 34 30" fill="none" stroke="#fff" stroke-width="1.6" stroke-linejoin="round">
        <path d="M3 12l7-5 6 3 6-3 9 5"/><path d="M6 14l7 8a2 2 0 0 0 3 0l2-2 2 2a2 2 0 0 0 3-1l5-7"/><path d="M13 14l4 4"/>
      </svg>Partnership</div>
    <div class="value value--tech">
      <svg width="30" height="30" viewBox="0 0 30 30" fill="none" stroke="#fff" stroke-width="1.6">
        <circle cx="15" cy="15" r="6"/><circle cx="15" cy="15" r="2"/>
        <path d="M15 3v4M15 23v4M3 15h4M23 15h4M6.5 6.5l3 3M20.5 20.5l3 3M6.5 23.5l3-3M20.5 9.5l3-3"/>
      </svg>Innovative<br>Technology</div>
    <div class="value value--quality">
      <svg width="30" height="30" viewBox="0 0 30 30" fill="none" stroke="#fff" stroke-width="1.6">
        <circle cx="15" cy="15" r="12"/><circle cx="15" cy="15" r="8"/><path d="M11 15l3 3 5-6"/>
      </svg>Premium<br>Quality</div>
    <div class="value value--battery">
      <svg width="36" height="26" viewBox="0 0 36 26" fill="none" stroke="#fff" stroke-width="1.6" stroke-linejoin="round">
        <rect x="2" y="4" width="28" height="18" rx="2"/><path d="M30 10h3v6h-3"/><path d="M18 6l-5 8h5l-3 7 7-9h-5l3-6z"/>
      </svg>Battery-<br>Power</div>
  </div>
</section>

</body>
</html>
```